Postcard, Logo, and Website Design for Direct to Consumer Personal Bankruptcy Service

We are launching a bankruptcy legal practice. Our postcard design will be mailed to prospective clients who have already been sued by their credit card companies.

We would like people to glean from the post card that they can call to set up a no-fee consultation, or to phone our offices, where our receptionist can aid them in setting up a no-fee consultation.

Logo should be professional, but not overly stuffy.

Website copy can be added later, but most important is a space where people can fill out there info so we can reach out to them.

Pertinent info that should be on postcard

Name: Lakeshore Fresh Start Legal
Phone: 616-372-5819
Website: LFSLegalAid.com

Rough ideas that we've tossed around include the following (but use your own judgement - we're counting on you for creativity):

Creditors Calling?
Mountain of Debt?
Getting Sued?

We can help!

Target Market(s)

People who are thinking about bankruptcy and have already been sued

Industry/Entity Type

Financial Service

Logo Text

Lakeshore Fresh Start Legal

Number of Pages Required

1 page

Font styles to use
Sans Serif

Colors

Designer to choose colors to be used in the design.

Requirements
Must have
• Space for info about bankruptcy process
• Space for user to submit info

```html
<!DOCTYPE html>
<html lang="en">
<head>
<meta charset="utf-8">
<title>Lakeshore Fresh Start Legal – Postcard</title>
<link rel="stylesheet" href="https://fonts.googleapis.com/css2?family=Arimo:wght@400;700&family=Open+Sans:wght@400&display=swap">
<style>
  :root {
    --backdrop: #585858;
    --paper: #ffffff;
    --teal: #36bab3;
    --navy: #1f3b58;
    --ink: #1b1b1b;
    --band: #1e1e1e;
    --photo-warm-a: #d8cfc2;
    --photo-warm-b: #8f7a65;
    --photo-dark-a: #4a4845;
    --photo-dark-b: #6b665e;
    --rule: #cfcfcf;
    --label: #f2f2f2;
  }
  * { box-sizing: border-box; margin: 0; padding: 0; }
  html, body { width: 850px; height: 1200px; overflow: hidden; }
  body {
    background: var(--backdrop);
    position: relative;
    font-family: "Arimo", Arial, sans-serif;
  }
  .postcard {
    position: absolute;
    left: 118px;
    width: 612px;
    height: 394px;
    background: var(--paper);
    box-shadow: 0 6px 14px rgba(0,0,0,.45);
    overflow: hidden;
  }
  .postcard--front { top: 113px; }
  .postcard--back { top: 645px; }
  .postcard__shapes { position: absolute; inset: 0; }
  .abs { position: absolute; line-height: 1; white-space: nowrap; }

  .side-label {
    position: absolute;
    width: 200px;
    text-align: center;
    font-family: "Open Sans", Arial, sans-serif;
    font-size: 32px;
    color: var(--label);
    line-height: 1;
  }

  /* front */
  .brand-name { color: var(--teal); font-size: 16px; }
  .concerns { list-style: none; }
  .concern { position: absolute; left: 17px; display: flex; align-items: center; gap: 8px; font-size: 18px; color: var(--navy); }
  .concern__num {
    width: 15px; height: 15px; border-radius: 50%;
    background: var(--navy); color: #fff; font-size: 10px;
    display: flex; align-items: center; justify-content: center;
  }
  .concern b { font-weight: 700; }
  .headline { left: 17px; top: 200px; font-size: 34px; color: var(--navy); }
  .intro { left: 17px; top: 246px; width: 250px; font-size: 11px; line-height: 14px; color: var(--ink); white-space: normal; }
  .call-label { left: 15px; top: 302px; font-size: 24px; color: var(--teal); }
  .phone-front { left: 52px; top: 355px; font-size: 21px; font-weight: 700; color: #fff; }
  .firm-name { left: 233px; width: 400px; text-align: center; top: 305px; font-size: 24px; color: #fff; }
  .web-front { left: 233px; width: 400px; text-align: center; top: 361px; font-size: 22px; color: #fff; }

  /* back */
  .about-firm { left: 23px; top: 30px; font-size: 18px; color: #fff; }
  .about-title { left: 23px; top: 59px; font-size: 24px; color: #fff; }
  .about-body { left: 23px; top: 98px; width: 205px; font-size: 11.5px; line-height: 14.3px; color: #fff; white-space: normal; }
  .brand-name--back { left: 388px; width: 100px; text-align: center; top: 67px; font-size: 13px; }
  .contact-back { left: 58px; font-weight: 700; color: #fff; }
</style>
</head>
<body>

<section class="postcard postcard--front" aria-label="Postcard front">
  <svg class="postcard__shapes" width="612" height="394" viewBox="0 0 612 394" aria-hidden="false">
    <defs>
      <linearGradient id="libraryTone" x1="0" y1="0" x2="1" y2="1">
        <stop offset="0" stop-color="var(--photo-warm-a)"/>
        <stop offset="1" stop-color="var(--photo-warm-b)"/>
      </linearGradient>
    </defs>
    <polygon role="img" aria-label="Photo of law books, scales of justice and a gavel on a desk" points="262,0 612,0 612,272 358,272" fill="url(#libraryTone)"/>
    <polygon points="245,0 268,0 350,225 327,225" fill="var(--teal)"/>
    <rect x="260" y="274" width="255" height="11" fill="var(--navy)"/>
    <polygon points="247,290 612,287 612,394 217,394" fill="var(--teal)"/>
    <polygon points="0,332 237,332 212,394 0,394" fill="var(--band)"/>
    <!-- phone icon -->
    <g transform="translate(29 365)" fill="none" stroke="#fff" stroke-width="1.6">
      <circle r="11"/>
      <path d="M-4,-5 l2,-1 2,3 -1.5,1.5 q1,2.5 3,3.5 l1.5,-1.5 3,2 -1,2 q-5,1 -9,-9z" fill="#fff" stroke="none"/>
    </g>
    <!-- globe icon -->
    <g transform="translate(433 345)" fill="none" stroke="#fff" stroke-width="1.3">
      <circle r="9"/>
      <ellipse rx="4" ry="9"/>
      <line x1="-9" y1="0" x2="9" y2="0"/>
      <line x1="-8" y1="-4" x2="8" y2="-4"/>
      <line x1="-8" y1="4" x2="8" y2="4"/>
    </g>
  </svg>

  <span class="abs brand-name" style="left:17px; top:81px;">LFSLegal</span>

  <ul class="concerns">
    <li class="concern" style="top:110px;"><span class="concern__num">1</span><span>Creditors <b>CALLING?</b></span></li>
    <li class="concern" style="top:138px;"><span class="concern__num">2</span><span>Mountain of <b>DEBT?</b></span></li>
    <li class="concern" style="top:164px;"><span class="concern__num">3</span><span>Getting <b>SUED?</b></span></li>
  </ul>

  <h1 class="abs headline" style="font-weight:400;">We can help!</h1>
  <p class="abs intro">Lorem ipsum dolor sit amet, consectetur adipiscing elit. Suspendisse vel consectetur sem, non tempus libero.</p>
  <p class="abs call-label">Call us:</p>
  <p class="abs phone-front">616-372-5819</p>
  <p class="abs firm-name">Lakeshore Fresh Start Legal</p>
  <p class="abs web-front">LFSLegalAid.com</p>
</section>

<p class="side-label" style="left:318px; top:555px;">Front</p>

<section class="postcard postcard--back" aria-label="Postcard back">
  <svg class="postcard__shapes" width="612" height="394" viewBox="0 0 612 394">
    <defs>
      <linearGradient id="officeTone" x1="0" y1="0" x2="1" y2="1">
        <stop offset="0" stop-color="var(--photo-dark-a)"/>
        <stop offset="1" stop-color="var(--photo-dark-b)"/>
      </linearGradient>
    </defs>
    <polygon role="img" aria-label="Dimmed photo of a justice statue in a law office" points="0,0 300,0 228,265 0,265" fill="url(#officeTone)"/>
    <polygon points="302,0 322,0 250,215 230,215" fill="var(--navy)"/>
    <polygon points="325,0 340,0 262,215 247,215" fill="var(--teal)"/>
    <line x1="23" y1="88" x2="177" y2="88" stroke="#e0e0e0" stroke-width="1"/>
    <polygon points="0,290 302,290 344,394 0,394" fill="var(--teal)"/>
    <polygon points="0,283 245,283 250,296 0,296" fill="var(--navy)"/>
    <rect x="524.5" y="20.5" width="58" height="57" fill="none" stroke="var(--rule)"/>
    <g stroke="var(--rule)" stroke-width="1">
      <line x1="376" y1="170" x2="582" y2="170"/>
      <line x1="376" y1="193" x2="582" y2="193"/>
      <line x1="376" y1="216" x2="582" y2="216"/>
      <line x1="376" y1="239" x2="582" y2="239"/>
    </g>
    <g transform="translate(34 332)" fill="none" stroke="#fff" stroke-width="1.5">
      <circle r="11"/>
      <ellipse rx="4.5" ry="8"/>
      <line x1="-8" y1="0" x2="8" y2="0"/>
      <line x1="-7" y1="-4" x2="7" y2="-4"/>
      <line x1="-7" y1="4" x2="7" y2="4"/>
    </g>
    <g transform="translate(34 365)" fill="none" stroke="#fff" stroke-width="1.5">
      <circle r="11"/>
      <path d="M-4,-5 l2,-1 2,3 -1.5,1.5 q1,2.5 3,3.5 l1.5,-1.5 3,2 -1,2 q-5,1 -9,-9z" fill="#fff" stroke="none"/>
    </g>
  </svg>

  <p class="abs about-firm">Lakeshore Fresh Start Legal</p>
  <h2 class="abs about-title" style="font-weight:400;">About us</h2>
  <p class="abs about-body">Lorem ipsum dolor sit amet,consectetur adipiscing elit. Nunc quam nibh, posuere sed dolor ac, finibus iaculis urna. Nulla vehicula leo ut scelerisque rutrum. Cras bibendum metus vitae magna vulputate, nec gravida dui interdum.Maecenas convallis orci risus, rutrum accumsan urna fringilla id.</p>

  <span class="abs brand-name brand-name--back">LFSLegal</span>

  <p class="abs contact-back" style="top:321px; font-size:22px; font-weight:400;">LFSLegalAid.com</p>
  <p class="abs contact-back" style="top:355px; font-size:21px;">616-372-5819</p>
</section>

<p class="side-label" style="left:327px; top:1085px;">Back</p>

</body>
</html>
```